Need cover for book about the Cold Hooks child sex traffickers play with their victims

We train professionals, first responders, parents, foster parents, and others about child sex trafficking in the United States. This book is based on the life story of a former 32-year child sex trafficker who sold more than 150 children and women in all 50 states, Canada, and Europe. The book will not only help prevent kids from becoming victims of people like he was, but it also will prevent youth from becoming traffickers, as well.

```html
<!DOCTYPE html>
<html lang="en">
<head>
<meta charset="utf-8">
<title>Cold Hooks – Book Cover</title>
<link href="https://fonts.googleapis.com/css2?family=Exo+2:ital,wght@0,400;0,500;0,600;1,300;1,400&display=swap" rel="stylesheet">
<style>
  :root {
    --backdrop: #e9e9e9;
    --cover-black: #050506;
    --ink-white: #f2f2f2;
    --figure-top: #f4f4f4;
    --figure-mid: #8a8a8a;
    --figure-bottom: #1a1a1a;
  }
  * { margin: 0; padding: 0; box-sizing: border-box; }
  html, body {
    width: 1200px; height: 1200px; overflow: hidden;
    background: var(--backdrop);
    font-family: "Exo 2", sans-serif;
  }
  .book-cover {
    position: absolute; left: 235px; top: 40px;
    width: 730px; height: 1120px;
    background: var(--cover-black);
    color: var(--ink-white);
  }
  .foreword {
    position: absolute; top: 60px; left: 0; width: 100%;
    text-align: center; font-style: italic; font-weight: 300;
    font-size: 19px; line-height: 27px;
  }
  .foreword .foreword-name {
    font-style: normal; font-weight: 600; font-size: 26px;
  }
  .figure-art {
    position: absolute; left: 252px; top: 225px;
    width: 226px; height: 125px;
    background: linear-gradient(180deg, var(--figure-top) 0%, var(--figure-mid) 45%, var(--figure-bottom) 100%);
    border-radius: 60px 60px 6px 6px;
  }
  .title {
    position: absolute; left: 0; width: 100%;
    text-align: center; font-weight: 400; line-height: 1;
    font-size: 180px; letter-spacing: 2px;
  }
  .title-line-one { top: 355px; }
  .title-line-two { top: 545px; }
  .subtitle {
    position: absolute; top: 780px; left: 0; width: 100%;
    text-align: center; font-style: italic; font-weight: 400;
    font-size: 30px; line-height: 38px;
  }
  .author {
    position: absolute; top: 960px; left: 0; width: 100%;
    text-align: center; font-weight: 500; font-size: 56px; line-height: 1;
  }
  .co-author {
    position: absolute; top: 1036px; left: 0; width: 100%;
    text-align: center; font-size: 20px; font-weight: 400;
  }
  .co-author em { font-weight: 300; }
</style>
</head>
<body>
  <main class="book-cover">
    <p class="foreword">
      With forward by <span class="foreword-name">Marla Quinn,</span><br>
      Dale's longtime victim and bottom<br>
      and creator of the Own Your Path program
    </p>

    <div class="figure-art" role="img" aria-label="Illustration of a faceless man in a white fedora and dark suit with a red tie"></div>

    <h1 class="title title-line-one">COLD</h1>
    <p class="title title-line-two">HOOKS</p>

    <p class="subtitle">Recognizing Trafficker<br>Manipulation Tactics</p>

    <p class="author">Dr. Renata Vale</p>
    <p class="co-author">and Dale Harmon, <em>a former 32-year child sex trafficker</em></p>
  </main>
</body>
</html>
```